Home page web design for a lawn specialist business

-The design must be based around the attached HPID (home page information design) called Turf Tidings HPID. I've attached Word and PDF versions - these are the same. The table boxes are just for approximate placement of information and you can use boxes and bold shapes for this design.

All fonts used in the HPID are only examples - you can use any Google font you wish.

- Text that is in orange is for your information only. Text to go on the design is black. Some instructions are in the HPID. Please be creative!

-The design needs to be modern and exciting - colours are to be the green of the logo, and white ...and then choose dark green, or dark grey or black.

Logo - attached (it's not great quality but don't worry, we'll replace it later)

- I've provided the images for the galleries - they are labelled and will match the name in the HPID. Please use the supplied images!

- Examples of some websites that have great design... don't copy them please but they are similar in look to what we are after....
www.qmbbuildworks.co.nz
http://www.rim-safeguard.co.nz/
http://www.lumenhomes.wb.gs/

Important: Width of content will be 1280 pixels when implemented as a web page but the winning design will need to supplied be on a 2000 pixel wide background so nav bars and background can extend outside the 1280 width.
Header height (without nav bar) 150-160 pixels.

We don't comment on individual designs but will choose a winning design promptly.

Industry/Entity Type

Business

Number of Pages Required

1 page

Font styles to use
Sans Serif

Requirements
Must have
• clean, modern, well-spaced design

```html
<!DOCTYPE html>
<html lang="en">
<head>
<meta charset="utf-8">
<title>Turf Tidings – Lawn Specialists</title>
<link rel="stylesheet" href="https://fonts.googleapis.com/css2?family=Oswald:wght@400;500&family=Open+Sans:wght@400;600;700&display=swap">
<style>
:root{
  --green:#6fa112;
  --green-dark:#4f7f0c;
  --ink:#1e1e1e;
  --text:#3a3a3a;
  --grey-bg:#e9e9e9;
  --grey-panel:#e0e0e0;
  --black:#141414;
  --white:#fff;
}
*{box-sizing:border-box;margin:0;padding:0}
html,body{width:678px;height:1200px;overflow:hidden;background:var(--white)}
body{position:relative;font-family:'Open Sans',Arial,sans-serif;color:var(--text)}
.abs{position:absolute}
.heading{font-family:'Oswald',Arial,sans-serif;font-weight:400;text-transform:uppercase;color:var(--ink)}

/* header */
.site-header{left:0;top:0;width:678px;height:46px;background:linear-gradient(#fff 0%,#fff 55%,#e2e2e2 100%)}
.brand{left:148px;top:9px;display:flex;align-items:center;gap:5px}
.brand-mark{width:15px;height:15px;background:var(--green)}
.brand-name{font-family:'Oswald',Arial,sans-serif;font-size:15px;font-weight:500;color:var(--green)}
.header-info{right:146px;top:4px;text-align:right;line-height:1}
.header-info .title{font-family:'Oswald',Arial,sans-serif;font-size:9.5px;color:var(--green);font-weight:500}
.header-info .tag{font-size:5px;color:var(--ink);margin-top:2px}
.header-info .region{font-size:4.3px;color:#555;margin-top:2px}
.header-info .phone{font-family:'Oswald',Arial,sans-serif;font-size:9.5px;color:var(--ink);margin-top:2px}

/* nav */
.main-nav{left:0;top:46px;width:678px;height:15px;background:var(--green)}
.main-nav ul{list-style:none;position:absolute;left:150px;top:0;display:flex;height:15px}
.main-nav li{font-family:'Oswald',Arial,sans-serif;font-size:4.8px;color:var(--white);text-transform:uppercase;padding:0 5.4px;line-height:15px}
.main-nav li.active{background:var(--black)}

/* hero */
.hero{left:0;top:61px;width:678px;height:207px;background:var(--black)}
.hero-frame{left:146px;top:9px;width:386px;height:189px;background:var(--white);padding:2px}
.hero-photo{width:100%;height:100%;background:
  linear-gradient(100deg,#d8d6d0 0%,#8a7563 12%,#6f5a48 42%,#e8e6e0 47%,#e8e6e0 49%,#4a8f2a 53%,#3f8a22 80%,#357a1c 100%)}
.tag-before,.tag-after{font-family:'Oswald',Arial,sans-serif;font-size:7.5px;color:#fff;text-align:center;line-height:13px}
.tag-before{left:295px;top:148px;width:50px;height:13px;background:var(--green)}
.tag-after{left:332px;top:166px;width:50px;height:13px;background:var(--black)}

/* intro */
.intro{left:146px;top:281px;width:386px;text-align:center}
.intro h1{font-size:12px;color:var(--green);font-weight:500}
.intro .lead{font-size:5.8px;color:var(--ink);font-weight:600;margin-top:1px}
.intro p.body{text-align:left;font-size:4.6px;line-height:7.6px;margin-top:11px;color:var(--text)}

/* services */
.services{left:0;top:378px;width:678px;height:352px;background:var(--grey-bg)}
.card{width:188px;height:154px;background:var(--white)}
.card h2{position:absolute;left:10px;top:10px;font-size:7px}
.card .photo{position:absolute;left:10px;top:27px;width:168px;height:67px}
.card p{position:absolute;left:10px;top:101px;width:168px;font-size:4.6px;line-height:7.6px;color:var(--text)}
.card .btn{position:absolute;left:0;bottom:0;width:188px;height:15px;background:var(--green);color:var(--white);font-size:4.8px;font-weight:700;text-transform:uppercase;text-align:center;line-height:15px}

/* video */
.video-title{left:146px;top:745px;width:254px;font-size:8.4px;line-height:9.8px}
.video{left:146px;top:773px;width:254px;height:143px;background:
  linear-gradient(180deg,#3e5a30 0%,#6f7a6e 25%,#4f6e38 45%,#5f9a30 60%,#6aa838 100%)}
.video svg{position:absolute;left:112px;top:56px}
.aside{left:410px;top:746px;width:122px;height:170px;background:var(--grey-panel);padding:10px 10px}
.aside h3{font-size:9.5px}
.aside p{font-size:4.6px;line-height:7.6px;margin-top:8px;color:var(--text)}
.aside .more{position:absolute;right:0;bottom:0;width:56px;height:12px;background:var(--white);color:var(--green);font-size:4.8px;font-weight:700;text-align:center;line-height:12px}

/* testimonial */
.testimonial{left:0;top:932px;width:678px;height:96px;background:var(--green)}
.testimonial h2{position:absolute;left:146px;top:18px;width:204px;font-size:8.4px;line-height:9.4px;color:var(--white)}
.testimonial blockquote{position:absolute;left:146px;top:43px;width:202px;font-size:4.6px;line-height:7.4px;color:#fff}
.testimonial .cite{position:absolute;left:290px;top:65px;font-size:4.6px;line-height:6.4px;color:#1c2a0a}
.testimonial .cite b{color:#fff;font-weight:600}
.testimonial .photo{position:absolute;left:352px;top:18px;width:180px;height:60px;background:
  linear-gradient(90deg,#7a7f70 0%,#5f8f36 30%,#7fb542 60%,#9ccb5a 100%)}

/* footer */
.site-footer{left:0;top:1028px;width:678px;height:137px;background:var(--grey-bg)}
.footer-links{position:absolute;left:146px;top:14px;list-style:none}
.footer-links li{font-size:4.8px;line-height:10.2px;color:var(--ink)}
.badge{position:absolute;left:241px;top:22px;width:60px;height:62px;background:#9cc83a;border-radius:50%}
.quote{position:absolute;left:344px;top:13px;width:188px}
.quote h3{font-size:6.4px;line-height:7.6px}
.quote h3 span{color:var(--green)}
.field{position:absolute;height:12px;background:var(--white);border:1px solid #d0d0d0;font-size:4.4px;color:#777;padding-left:3px;line-height:10px}
.field.area{height:33px}
.quote .send{position:absolute;left:141px;top:93px;width:47px;height:12px;background:var(--black);color:var(--white);font-family:'Oswald',Arial,sans-serif;font-size:5.4px;text-align:center;line-height:12px}
.copyright{position:absolute;left:0;top:128px;width:678px;text-align:center;font-size:4.4px;color:#555}
.grass-edge{left:0;top:1165px;width:678px;height:35px;background:linear-gradient(#f4f4f4 0%,#cfe39c 25%,#7fb23a 60%,#3f6e1a 100%)}
</style>
</head>
<body>

<header class="site-header abs">
  <div class="brand abs"><span class="brand-mark"></span><span class="brand-name">Turf Tidings</span></div>
  <div class="header-info abs">
    <div class="title">LAWN SPECIALISTS</div>
    <div class="tag">...from ground preparation to lawnaftercare</div>
    <div class="region">Servicing the Auckland region</div>
    <div class="phone">0800 44 66 00</div>
  </div>
</header>

<nav class="main-nav abs">
  <ul>
    <li class="active">Home</li><li>About us</li><li>Services</li><li>Lawn care</li><li>Seasonal care</li><li>Hydroseeding</li><li>FAQs</li><li>Before &amp; After Gallery</li><li>Quote / Contact</li>
  </ul>
</nav>

<section class="hero abs">
  <div class="hero-frame abs"><div class="hero-photo" role="img" aria-label="Garden before and after lawn installation, bare soil beside fresh green grass"></div></div>
</section>
<div class="tag-before abs">BEFORE</div>
<div class="tag-after abs">AFTER</div>

<section class="intro abs">
  <h1 class="heading">You can always spot a Turf Tidings lawn</h1>
  <div class="lead">It's the one that turns your neighbours green with envy.</div>
  <p class="body">If you want a lawn or playing field that looks good throughout the year, talk to us. Turf Tidings are New Zealand's experts in high quality grass seeding and lawn maintenance, creating the lushest lawns you'll ever see. With high-tech equipment, years of experience and expert aftercare, nobody knows grass like Turf Tidings.</p>
  <p class="body" style="margin-top:6px">There are many factors that influence the quality of a lawn, including seasonality, growing conditions, shade, seed types, and time. A one-size-fits-all solution couldn't possibly guarantee a great lawn, so we provide personalised advice, a full range of seeding techniques</p>
</section>

<section class="services abs">
  <article class="card abs" style="left:146px;top:16px">
    <h2 class="heading">Grass seeding services</h2>
    <div class="photo" style="background:linear-gradient(#4e5a3a 0%,#6f7a50 30%,#3f9a88 50%,#2f8f80 100%)" role="img" aria-label="Freshly hydroseeded garden bed"></div>
    <p>With a wide range of grass seed applications to choose from, including hydroseeding and instant lawn, there is an option to suit your property and your requirements.</p>
    <div class="btn">More about grass seeding</div>
  </article>
  <article class="card abs" style="left:344px;top:16px">
    <h2 class="heading">Lawn care maintenance</h2>
    <div class="photo" style="background:radial-gradient(circle at 55% 50%,#c9d8b0 0%,#8dbf3f 25%,#5e9a22 60%,#3f7014 100%)" role="img" aria-label="Sprinkler watering a green lawn"></div>
    <p>As well as lawn care services, the team at Turf Tidings provides helpful information for regular upkeep of your residential or commercial lawn.</p>
    <div class="btn">More about ongoing lawn care</div>
  </article>
  <article class="card abs" style="left:146px;top:180px">
    <h2 class="heading">FAQs about grass seeding and lawn care</h2>
    <div class="photo" style="background:linear-gradient(#c9c3b3 0%,#9a9a80 28%,#4f9a2a 45%,#3f8a22 85%,#d8d6d0 100%)" role="img" aria-label="Green lawn in a fenced garden"></div>
    <p>For more information, read our frequently asked questions regarding grass seeding and lawn care.</p>
    <div class="btn">Grass seeding &amp; lawn care FAQs</div>
  </article>
  <article class="card abs" style="left:344px;top:180px">
    <h2 class="heading">Before and after lawn photos</h2>
    <div class="photo" style="background:linear-gradient(90deg,#4f8a80 0%,#3f8a7f 49%,#fff 49.5%,#fff 50.5%,#5ca032 51%,#6aa83a 100%)" role="img" aria-label="Lawn area before and after seeding"></div>
    <p>See what you potential new lawn could look like by viewing a range of before and after lawn seeding photos.</p>
    <div class="btn">Before and after photos</div>
  </article>
</section>

<h2 class="video-title heading abs">Watch the video on how Turf Tidings can transform your empty spaces into beautiful green grass lawns</h2>
<div class="video abs" role="img" aria-label="Video still of a new lawn in front of a house">
  <svg width="30" height="30" viewBox="0 0 30 30"><circle cx="15" cy="15" r="13" fill="none" stroke="#fff" stroke-width="2"/><path d="M12 9 L21 15 L12 21 Z" fill="#fff"/></svg>
</div>
<aside class="aside abs">
  <h3 class="heading">Turf Tidings...</h3>
  <p>For all things grass, you need the best! Turf Tidings are skilled specialists when it comes to creating the perfect lawn for your property.</p>
  <p>From pre-seeding preparation to a full range of grass seeding services and lawn after care options, you'll enjoy a healthy green lawn for many years.</p>
  <p>Selling your property? Turf Tidings will add the wow factor to the outdoor areas of your home with a lush green lawn.</p>
  <div class="more">FIND OUT MORE</div>
</aside>

<section class="testimonial abs">
  <h2 class="heading">Watch the video on how Turf Tidings can transform your empty spaces into beautiful green grass lawns</h2>
  <blockquote>"Testimonial here about how great Turf Tidings were to deal with and how they are so happy with the lawn and the after care services etc etc."</blockquote>
  <div class="cite"><b>- Tom Carver</b><br>&nbsp;&nbsp;Homeowner, Albany</div>
  <div class="photo" role="img" aria-label="Lawn mower on freshly cut grass"></div>
</section>

<footer class="site-footer abs">
  <ul class="footer-links">
    <li>Home</li><li>About us</li><li>Services</li><li>Lawn care</li><li>Seasonal care</li><li>Hydroseeding</li><li>FAQs</li><li>Before &amp; After Gallery</li><li>Quote / Contact</li>
  </ul>
  <div class="badge" role="img" aria-label="Horticulture qualification badge"></div>
  <div class="quote">
    <h3 class="heading">Get a quote for your new lawn!<br>Fill in the form or phone us on <span>0800 44 66 00</span></h3>
    <div class="field" style="left:0;top:26px;width:92px">First Name</div>
    <div class="field" style="left:96px;top:26px;width:92px">Last Name</div>
    <div class="field" style="left:0;top:41px;width:92px">Email Address</div>
    <div class="field" style="left:96px;top:41px;width:92px">Contact Phone</div>
    <div class="field area" style="left:0;top:57px;width:188px">Details</div>
    <div class="send">CALL ME BACK</div>
  </div>
  <div class="copyright">Copyright © 2015 Turf Tidings. All Rights Reserved.</div>
</footer>

<div class="grass-edge abs" role="img" aria-label="Strip of grass blades along the page bottom"></div>

</body>
</html>
```